Orva Business Card

we need a business card for flooring business called Orva Flooring, the design should be black and white. we have 2 locations

Nunawading Showroom
527 Kellerman Road,
Nunawading VIC 3131

Bentleigh Showroom
462 Bramwell Hwy,
Bentleigh VIC 3204

email : sales@orvaflooring.com.au
(03) 9471 2830

Please inform we sell , Laminate, Hybrid, Timber, carpet and commercial flooring

```html
<!DOCTYPE html>
<html lang="en">
<head>
<meta charset="UTF-8">
<title>Orva Flooring Business Card</title>
<link href="https://fonts.googleapis.com/css2?family=Montserrat:wght@400&display=swap" rel="stylesheet">
<style>
  :root {
    --page-bg: #e9e7e4;
    --card-bg: #2a2828;
    --ink: #ffffff;
    --ink-soft: #d9d9d9;
    --ink-muted: #bdbdbd;
    --rule: #cfcfcf;
    --shadow: rgba(0, 0, 0, 0.28);
  }
  * { box-sizing: border-box; margin: 0; padding: 0; }
  html, body {
    width: 1187px;
    height: 1200px;
    overflow: hidden;
    background: var(--page-bg);
    font-family: "Montserrat", Arial, sans-serif;
  }
  .sheet {
    width: 1187px;
    height: 1200px;
    display: flex;
    flex-direction: column;
    align-items: center;
    justify-content: center;
    gap: 64px;
  }
  .card {
    width: 880px;
    height: 503px;
    background: var(--card-bg);
    box-shadow: 0 10px 28px var(--shadow);
    position: relative;
    color: var(--ink);
  }
  .card-front {
    display: flex;
    flex-direction: column;
    align-items: center;
    justify-content: center;
    gap: 26px;
  }
  .brand-name {
    font-weight: 400;
    font-size: 62px;
    letter-spacing: 1px;
    color: var(--ink);
    display: flex;
    align-items: center;
    gap: 18px;
  }
  .brand-mark {
    width: 22px;
    height: 22px;
    border-radius: 50%;
    background: var(--ink);
    flex: none;
  }
  .product-list {
    font-size: 17px;
    letter-spacing: 2px;
    text-transform: uppercase;
    color: var(--ink-muted);
  }
  .card-back {
    display: flex;
    align-items: center;
  }
  .back-brand {
    width: 435px;
    display: flex;
    justify-content: center;
  }
  .back-brand .brand-name {
    font-size: 38px;
    gap: 14px;
    color: var(--ink-soft);
  }
  .back-brand .brand-mark {
    width: 14px;
    height: 14px;
    background: var(--ink-soft);
  }
  .divider {
    width: 2px;
    height: 258px;
    background: var(--rule);
  }
  .contact {
    padding-left: 46px;
    font-size: 21px;
    line-height: 31px;
    color: var(--ink);
  }
  .showroom { margin-bottom: 12px; }
  .contact-line {
    display: flex;
    align-items: center;
    gap: 8px;
  }
  .contact-line + .contact-line { margin-top: 4px; }
  .icon { width: 17px; height: 17px; fill: var(--ink); flex: none; }
</style>
</head>
<body>
  <main class="sheet">
    <section class="card card-front" aria-label="Card front">
      <div class="brand-name"><span class="brand-mark"></span>Orva Flooring</div>
      <p class="product-list">Laminate · Hybrid · Timber · Carpet · Commercial</p>
    </section>

    <section class="card card-back" aria-label="Card back">
      <div class="back-brand">
        <div class="brand-name"><span class="brand-mark"></span>Orva Flooring</div>
      </div>
      <div class="divider"></div>
      <div class="contact">
        <p class="showroom">Nunawading Showroom<br>527 Kellerman Road,<br>Nunawading VIC 3131</p>
        <p class="showroom">Bentleigh Showroom<br>462 Bramwell Hwy,<br>Bentleigh VIC 3204</p>
        <p class="contact-line">
          <svg class="icon" viewBox="0 0 24 24" aria-hidden="true"><path d="M6.6 10.8a15.1 15.1 0 0 0 6.6 6.6l2.2-2.2a1 1 0 0 1 1-.25 11.4 11.4 0 0 0 3.6.57 1 1 0 0 1 1 1V20a1 1 0 0 1-1 1A17 17 0 0 1 3 4a1 1 0 0 1 1-1h3.5a1 1 0 0 1 1 1c0 1.25.2 2.45.57 3.57a1 1 0 0 1-.25 1z"/></svg>
          (03) 9471 2830
        </p>
        <p class="contact-line">
          <svg class="icon" viewBox="0 0 24 24" aria-hidden="true"><path d="M2 6.2V19h20V6.2l-10 7.6z M2.8 5 12 12 21.2 5z"/></svg>
          sales@orvaflooring.com.au
        </p>
      </div>
    </section>
  </main>
</body>
</html>
```